Design Box Packaging with Logo for a high-end menswear store

I would like to come up with a design for our shipping boxes.
- Printing would only be in 1 colour. (box will be in mid beige/brown)
- I want it to look modern and clean
- I have attached my logo
- It is for a high-end menswear store for shipping clothing for online purchases
Size of the box is about 14 x 10 x 5

Target Market(s)

High-end / wealthy people shopping online

Industry/Entity Type

Clothing, retail, online high-end clothing

Colors

Designer to choose colors to be used in the design.

Requirements
Must have
• Look sharp and clean, have logo information, online printing one colour
Nice to have
• Look clean and modern

```html
<!DOCTYPE html>
<html lang="en">
<head>
<meta charset="utf-8">
<title>Maison Laurent — Shipping Box Artwork</title>
<link href="https://fonts.googleapis.com/css2?family=Montserrat:wght@500;700;900&display=swap" rel="stylesheet">
<style>
  :root {
    --ink: #0a0a9a;
    --kraft: #c9a27c;
    --kraft-shade: #bb9470;
    --paper: #ffffff;
    --stage: #f4f1ec;
    --note: #1a1a1a;
  }
  * { margin: 0; padding: 0; box-sizing: border-box; }
  html, body { width: 1043px; height: 1200px; overflow: hidden; }
  body {
    background: var(--paper);
    font-family: "Montserrat", Arial, sans-serif;
    color: var(--ink);
    position: relative;
  }
  .artwork {
    position: absolute; left: 52px; top: 52px;
    width: 939px; height: 703px;
    background: var(--stage);
  }
  .panel { position: absolute; background: var(--kraft); overflow: hidden; }
  .panel--top   { left: 40px;  top: 40px;  width: 600px; height: 300px; }
  .panel--front { left: 40px;  top: 345px; width: 600px; height: 290px; }
  .panel--side  { left: 645px; top: 345px; width: 250px; height: 290px; background: var(--kraft-shade); }

  .wave-field {
    position: absolute; left: 0; right: 0;
    background: repeating-linear-gradient(135deg, var(--ink) 0 9px, var(--kraft) 9px 14px);
  }
  .panel--top .wave-field   { top: 0; height: 140px; }
  .panel--front .wave-field { bottom: 0; height: 130px; }

  .shipping-label {
    position: absolute; left: 60px; top: 22px;
    width: 200px; height: 90px;
    background: var(--kraft);
    display: flex; align-items: center; justify-content: center;
    font-size: 8px; font-weight: 900; letter-spacing: .5px; text-transform: uppercase;
  }
  .store-url {
    position: absolute; left: 0; right: 0; top: 175px;
    text-align: center;
    font-size: 38px; font-weight: 900; letter-spacing: 1px; text-transform: uppercase;
  }
  .social-row {
    position: absolute; left: 0; right: 0; top: 245px;
    display: flex; justify-content: center; gap: 28px;
    font-size: 9px; font-weight: 700;
  }
  .social-row span, .side-social span { display: flex; align-items: center; gap: 5px; white-space: nowrap; }
  .dot { width: 9px; height: 9px; border-radius: 50%; background: var(--ink); display: inline-block; flex: none; }

  .brand-mark {
    position: absolute; left: 50%; top: 38px; transform: translateX(-50%);
    display: flex; align-items: center; gap: 10px;
    font-size: 22px; font-weight: 700; letter-spacing: 2px; white-space: nowrap;
  }
  .brand-mark .square { width: 18px; height: 18px; background: var(--ink); }

  .side-brand {
    position: absolute; left: 80px; top: 145px;
    transform: translate(-50%, -50%) rotate(-90deg);
    font-size: 20px; font-weight: 700; letter-spacing: 3px; white-space: nowrap;
    line-height: 1;
  }
  .side-social {
    position: absolute; left: 112px; bottom: 30px;
    display: flex; flex-direction: column; gap: 6px;
    font-size: 8px; font-weight: 700;
  }

  .preview-note {
    position: absolute; left: 0; right: 0; bottom: 14px;
    text-align: center; font-size: 10px; font-weight: 500; color: var(--note);
  }

  .pattern-swatch {
    position: absolute; left: 52px; top: 755px;
    width: 939px; height: 336px;
    background: repeating-linear-gradient(160deg, var(--ink) 0 34px, var(--paper) 34px 50px);
  }
</style>
</head>
<body>
  <section class="artwork">
    <div class="panel panel--top">
      <div class="wave-field" role="img" aria-label="Repeating blue wave pattern band"></div>
      <div class="shipping-label">Shipping label here</div>
      <div class="store-url">maisonlaurent.com</div>
      <div class="social-row">
        <span><i class="dot"></i>@maisonlaurent</span>
        <span><i class="dot"></i>Maison Laurent International</span>
      </div>
    </div>

    <div class="panel panel--front">
      <div class="brand-mark"><i class="square"></i>MAISON LAURENT</div>
      <div class="wave-field" role="img" aria-label="Repeating blue wave pattern band"></div>
    </div>

    <div class="panel panel--side">
      <div class="side-brand">MAISON LAURENT</div>
      <div class="side-social">
        <span><i class="dot"></i>@maisonlaurent</span>
        <span><i class="dot"></i>Maison Laurent Intl.</span>
      </div>
    </div>

    <p class="preview-note">**Mockup just for design preview only**</p>
  </section>

  <div class="pattern-swatch" role="img" aria-label="Repeat tile of the blue wave pattern on white"></div>
</body>
</html>
```